Custom Vinyl Wrap Design

I need a custom vinyl wrap design for a saw. This wrap is going to cover a saw that is used to cut stone. Please view the attached Jped document for my ideas and more design details.
Thank you.
Updates
The top and side of the saw should be one graphic because they are both one piece. The two ends of the saw should be two separate graphics. The "TusklineDrill Cutter" logo should be on the side of the saw. Please insure the Emergency Shut Off graphic is ergonomic and is more rectangular in shape as apposed to being a square label that takes up allot of room...
Hey guys, I am on a tight deadline for this project. It would be great to see some designs by the middle of the week if possible.
I would like to see some more graphics soon if possible. Dont worry about not getting all the dimensions exact for now. I just want to see everyone's individual style and interpretation of what I am looking for. Once I see everyone's style, I will chose the one designer to work closer with.
Target Market(s)
industrial, mining, construction
Requirements
Must have
- Branded logo
Made in Canada Logo
Eco friendly logo
Emergency Shut off label incorporated into the design
on-off-reset labels also incorporated into the design

```html
<!DOCTYPE html>
<html lang="en">
<head>
<meta charset="utf-8">
<title>TusklineDrill Cutter – Vinyl Wrap Panels</title>
<link href="https://fonts.googleapis.com/css2?family=Anton&family=Roboto:wght@400;700;900&display=swap" rel="stylesheet">
<style>
  :root {
    --page-bg: #ffffff;
    --ink: #111111;
    --panel-dark: #1b1b1b;
    --panel-mid: #5a5a5a;
    --panel-light: #9a9a9a;
    --blade-grey: #a9a9a9;
    --brand-blue: #1ea0dc;
    --brand-red: #e3141e;
    --brand-white: #ffffff;
    --label-yellow: #f4e21a;
    --label-green: #22b24c;
    --hazard-yellow: #f6e312;
  }
  * { margin: 0; padding: 0; box-sizing: border-box; }
  html, body { width: 1200px; height: 1188px; overflow: hidden; background: var(--page-bg); }
  .canvas { position: relative; width: 1200px; height: 1188px; font-family: "Roboto", Arial, sans-serif; color: var(--ink); }
  .panel-caption { position: absolute; font-size: 17px; font-weight: 400; white-space: nowrap; }
  .caption-left-top { left: 277px; top: 368px; }
  .caption-right-top { right: 190px; top: 362px; }
  .caption-side { right: 190px; top: 900px; }
  .wrap-art { position: absolute; left: 0; top: 0; }
  .label-card { position: absolute; background: var(--page-bg); box-shadow: 0 0 0 1px #e2e2e2; }
  .switch-card { left: 264px; top: 948px; width: 354px; height: 208px; }
  .back-card { left: 818px; top: 964px; width: 186px; height: 176px; }
  .label-card .panel-caption { position: static; padding: 6px 0 0 12px; display: block; }
  .label-card svg { position: absolute; }
  .brand-name { font-family: "Anton", Impact, sans-serif; fill: var(--brand-white); }
  .made-in { font-family: "Roboto", Arial, sans-serif; font-weight: 900; fill: var(--brand-white); }
  .stop-text { font-family: "Roboto", Arial, sans-serif; font-weight: 900; fill: var(--brand-white); }
  .switch-text { font-family: "Roboto", Arial, sans-serif; font-weight: 900; stroke: var(--ink); stroke-width: 1.2px; paint-order: stroke; }
  .caution-text { font-family: "Anton", Impact, sans-serif; fill: var(--ink); }
</style>
</head>
<body>
<main class="canvas">

  <span class="panel-caption caption-left-top">Saw Top - Left Side</span>
  <span class="panel-caption caption-right-top">Saw Top - Right Side</span>
  <span class="panel-caption caption-side">Saw Side Panel</span>

  <svg class="wrap-art" width="1200" height="1188" viewBox="0 0 1200 1188" aria-label="Saw top and side wrap panel">
    <defs>
      <clipPath id="wrap-shape">
        <path d="M231,393 H395 V715 H598 V393 H1010 V891 H231 Z"/>
      </clipPath>
      <linearGradient id="stone-texture" x1="0" y1="0" x2="1" y2="1">
        <stop offset="0" stop-color="var(--panel-dark)"/>
        <stop offset="0.45" stop-color="var(--panel-mid)"/>
        <stop offset="0.7" stop-color="var(--panel-light)"/>
        <stop offset="1" stop-color="var(--panel-dark)"/>
      </linearGradient>
    </defs>

    <g clip-path="url(#wrap-shape)">
      <rect x="231" y="393" width="779" height="498" fill="url(#stone-texture)" role="img" aria-label="Cracked stone grunge texture with red scratches"/>
      <polygon points="231,820 395,600 395,628 231,852" fill="var(--brand-blue)"/>
      <polygon points="231,393 240,393 240,470 231,480" fill="var(--brand-blue)"/>
      <polygon points="598,393 606,393 606,420 598,430" fill="var(--brand-blue)"/>
      <polygon points="545,891 585,891 880,393 850,393" fill="var(--brand-red)"/>
      <polygon points="610,891 628,891 935,393 917,393" fill="var(--brand-red)"/>
      <polygon points="960,640 1010,560 1010,585 975,645" fill="var(--brand-red)"/>
    </g>
    <path d="M231,393 H395 V715 H598 V393 H1010 V891 H231 Z" fill="none" stroke="var(--ink)" stroke-width="1.5"/>
    <line x1="231" y1="715" x2="1010" y2="715" stroke="var(--ink)" stroke-width="1.2"/>

    <path d="M396,715 A99,99 0 0 1 594,715 Z" fill="var(--blade-grey)"/>

    <g class="brand-lockup" transform="translate(660,870) rotate(-62)">
      <text class="brand-name" x="0" y="0" font-size="86" textLength="480" lengthAdjust="spacingAndGlyphs">TUSKLINEDRILL</text>
      <text class="brand-name" x="100" y="68" font-size="64" textLength="170" lengthAdjust="spacingAndGlyphs">CUTTER</text>
    </g>

    <circle cx="376" cy="836" r="37" fill="var(--brand-white)" stroke="var(--ink)" stroke-width="6"/>

    <g class="emergency-label">
      <rect x="878" y="607" width="128" height="82" rx="4" fill="var(--brand-white)"/>
      <rect x="884" y="613" width="116" height="70" fill="var(--brand-red)"/>
      <text class="stop-text" x="942" y="633" font-size="15" text-anchor="middle">EMERGENCY</text>
      <circle cx="942" cy="651" r="7" fill="var(--ink)"/>
      <text class="stop-text" x="942" y="677" font-size="15" text-anchor="middle">SHUT OFF</text>
    </g>

    <text class="made-in" x="789" y="877" font-size="21">MADE IN CANADA</text>
  </svg>

  <section class="label-card switch-card">
    <span class="panel-caption">Switch Panel</span>
    <svg style="left:11px;top:32px" width="332" height="172" viewBox="0 0 332 172" aria-label="Switch panel label">
      <rect x="0" y="0" width="332" height="172" fill="var(--ink)"/>
      <rect x="6" y="6" width="320" height="160" fill="var(--brand-blue)" role="img" aria-label="Blue panel with cracked black grunge texture"/>
      <text class="switch-text" x="64" y="28" font-size="19" fill="var(--label-yellow)" text-anchor="middle">SPEED</text>
      <rect x="65" y="41" width="51" height="110" fill="var(--blade-grey)" stroke="var(--ink)" stroke-width="2"/>
      <text class="switch-text" x="191" y="23" font-size="19" fill="var(--brand-red)" text-anchor="middle">OFF</text>
      <circle cx="187" cy="56" r="22" fill="var(--blade-grey)" stroke="var(--ink)" stroke-width="2"/>
      <text class="switch-text" x="253" y="23" font-size="19" fill="var(--label-green)" text-anchor="middle">ON</text>
      <circle cx="253" cy="56" r="22" fill="var(--blade-grey)" stroke="var(--ink)" stroke-width="2"/>
      <text class="switch-text" x="250" y="95" font-size="19" fill="var(--label-yellow)" text-anchor="middle">RESET</text>
      <circle cx="250" cy="122" r="22" fill="var(--blade-grey)" stroke="var(--ink)" stroke-width="2"/>
    </svg>
  </section>

  <section class="label-card back-card">
    <span class="panel-caption">Saw Back Panel</span>
    <svg style="left:11px;top:30px" width="164" height="140" viewBox="0 0 164 140" aria-label="Caution back panel label">
      <defs>
        <clipPath id="hazard-clip"><rect x="6" y="6" width="152" height="128"/></clipPath>
      </defs>
      <rect x="0" y="0" width="164" height="140" fill="var(--ink)"/>
      <g clip-path="url(#hazard-clip)" stroke="var(--hazard-yellow)" stroke-width="9">
        <line x1="-20" y1="40" x2="40" y2="-20"/>
        <line x1="-20" y1="70" x2="70" y2="-20"/>
        <line x1="-20" y1="100" x2="100" y2="-20"/>
        <line x1="-20" y1="130" x2="130" y2="-20"/>
        <line x1="-20" y1="160" x2="160" y2="-20"/>
        <line x1="10" y1="160" x2="190" y2="-20"/>
        <line x1="40" y1="160" x2="190" y2="10"/>
        <line x1="70" y1="160" x2="190" y2="40"/>
        <line x1="100" y1="160" x2="190" y2="70"/>
        <line x1="130" y1="160" x2="190" y2="100"/>
      </g>
      <g transform="translate(82,72) rotate(-35)">
        <rect x="-74" y="-24" width="148" height="48" fill="var(--brand-white)"/>
        <text class="caution-text" x="0" y="15" font-size="40" text-anchor="middle" textLength="136" lengthAdjust="spacingAndGlyphs">CAUTION</text>
      </g>
    </svg>
  </section>

</main>
</body>
</html>
```